New Web Design Project- Willowbrook Elders

Willowbrook Elders is the Capital regions premiere, non-medical, in-home care & companionship service that unites "junior-senior" caregivers with "senior-senior" care recipients so that senior-seniors can remain safe & independent in their own homes.
Our compassionate "junior-senior" caregivers are all retirees that have already enjoyed rewarding careers and/or have raised families of their own and feel the need to pay-it-forward with their care for older seniors.
Services include grocery shopping, medical or dental appointments, errands, meal preparation & cleanup, light housekeeping, bed making, laundry, hobbies, reading, transportation, entertainment, games, mobility assistance/transfers, respite care, light yard work, pet walking.

Target Market(s)

Grown children of senior-seniors between who are between 55-70, predominantly the daughters (female). End users of services (senior-seniors) are typically 80-100 years old and living in own homes

Industry/Entity Type

Medical

Coding

Coded - Design and coding required

Number of Pages Required

5+ page

Font styles to use
Sans Serif

Colors
3277b5
ec1f27

Requirements
Must have
• supporting photos on each page. Contact us page. Promotional video (done) attached that doesn't take viewers off my site (https://vidhost.example/q7Rk2mPzL4n).
• Also, need my downloadable brochure (attached).
• The following pages:
• Home. Services. About Us. News. Employment. Contact us. Junior-Seniors Assisting Senior-Seniors. Why non-medical in-home care. Who are junior-seniors?Financial effects of senior care. Do you need care? Does someone you love need care?
Should not have
• Any other photos or images other than what I've supplied.

```html
<!DOCTYPE html>
<html lang="en">
<head>
<meta charset="utf-8">
<title>Willowbrook Elders — Home</title>
<link rel="stylesheet" href="https://fonts.googleapis.com/css2?family=Montserrat:wght@400;600;700&family=Open+Sans:wght@400;600;700&display=swap">
<style>
:root{
  --brand-blue:#3277b5;
  --deep-blue:#1f4f95;
  --footer-blue:#2e62a9;
  --band-blue:#3169b0;
  --navy:#1d3a75;
  --red:#ec1f27;
  --ink:#333;
  --muted:#666;
  --grey-panel:#ececec;
  --white:#fff;
}
*{box-sizing:border-box;margin:0;padding:0}
html,body{width:1200px;height:2990px;overflow:hidden;background:var(--white)}
body{position:relative;font-family:"Open Sans",Arial,sans-serif;color:var(--ink)}
.abs{position:absolute}
.heading{font-family:"Montserrat",Arial,sans-serif;font-weight:700}

/* header */
.site-header{left:0;top:0;width:1200px;height:116px;background:var(--white)}
.brand{left:130px;top:18px;display:flex;flex-direction:column;align-items:flex-start}
.brand-mark{display:flex;align-items:center;gap:10px}
.brand-square{width:34px;height:34px;background:var(--navy)}
.brand-name{font-family:"Montserrat",Arial,sans-serif;font-weight:700;font-size:25px;color:var(--navy);letter-spacing:-.3px}
.brand-tag{font-size:11px;font-style:italic;color:var(--navy);margin-top:6px;margin-left:2px}
.call-now{left:780px;top:26px;display:flex;align-items:center;gap:14px}
.call-now .label{font-size:9px;font-weight:600;color:var(--navy);letter-spacing:.5px}
.call-now .number{font-family:"Montserrat",Arial,sans-serif;font-weight:700;font-size:19px;color:var(--navy)}
.follow{left:990px;top:22px}
.follow .label{font-size:9px;font-weight:600;color:var(--navy);letter-spacing:.5px;margin-bottom:5px}
.dots{display:flex;gap:4px}
.dot{width:22px;height:22px;border-radius:50%}
.main-nav{left:544px;top:82px;display:flex;align-items:center;gap:0;font-family:"Montserrat",Arial,sans-serif;font-size:11.5px;font-weight:600;color:var(--ink)}
.main-nav a{color:inherit;text-decoration:none;padding:5px 12px;margin-right:14px}
.main-nav a.active{background:var(--red);color:var(--white)}

/* hero */
.hero{left:0;top:116px;width:1200px;height:526px;background:linear-gradient(110deg,#8a7a62 0%,#c9b9a2 30%,#e8ddd0 55%,#8e9a6f 80%,#5d6a45 100%)}
.hero-shade{left:0;top:116px;width:1200px;height:526px;background:linear-gradient(to bottom,rgba(0,0,0,0) 45%,rgba(0,0,0,.35) 100%)}
.hero-arrow{top:346px;width:34px;height:38px;background:var(--brand-blue);display:flex;align-items:center;justify-content:center}
.hero-title{left:0;top:414px;width:1200px;text-align:center;color:var(--white);font-size:28px;line-height:38px;text-transform:uppercase;text-shadow:0 2px 6px rgba(0,0,0,.4)}
.btn-red{background:var(--red);color:var(--white);font-family:"Montserrat",Arial,sans-serif;font-weight:700;text-transform:uppercase;display:flex;align-items:center;justify-content:center}
.hero-btn{left:470px;top:510px;width:260px;height:50px;font-size:15px;border:2px solid rgba(255,255,255,.7)}

/* services */
.section-title{left:0;width:1200px;text-align:center;color:var(--brand-blue);font-size:20px;letter-spacing:.5px}
.title-rule{left:578px;width:44px;height:3px;background:var(--brand-blue)}
.service{top:796px;width:130px;text-align:center;font-size:14px;color:#555}
.service svg{display:block;margin:0 auto 20px}
.carousel-arrow{top:812px}

/* junior senior band */
.band-left{left:0;top:948px;width:714px;height:536px;background:var(--band-blue)}
.band-right{left:1068px;top:948px;width:132px;height:536px;background:var(--band-blue)}
.band-photo{left:714px;top:948px;width:354px;height:536px;background:linear-gradient(160deg,#6b5c4a,#a08d73 40%,#7fa05d 70%,#4f4035)}
.band-text{left:130px;top:986px;width:520px;color:var(--white)}
.band-text h2{font-family:"Open Sans",Arial,sans-serif;font-weight:600;font-size:27px;margin-bottom:6px}
.band-text .sub{font-size:15px;opacity:.92;margin-bottom:22px}
.band-text p{font-size:12.5px;line-height:20px}
.btn-white{left:132px;top:1174px;width:104px;height:30px;background:var(--white);color:var(--brand-blue);font-size:11px;font-weight:700;font-family:"Montserrat",Arial,sans-serif;display:flex;align-items:center;justify-content:center}
.benefits-label{left:130px;top:1254px;color:var(--white);font-size:14px;font-weight:600}
.benefits-rule{left:212px;top:1264px;width:498px;height:1px;background:rgba(255,255,255,.35)}
.benefit{width:190px;color:var(--white);font-size:12.5px;line-height:18px;display:flex;gap:10px}
.benefit svg{flex:none;margin-top:3px}

/* video */
.video-panel{left:714px;top:1484px;width:354px;height:472px;background:var(--grey-panel)}
.video-thumb{left:130px;top:1518px;width:554px;height:396px;background:linear-gradient(135deg,#5b4a3a,#9c8570 45%,#c7b6a0 65%,#4d4f62)}
.play{left:368px;top:1672px}
.promo-title{left:766px;top:1594px;color:var(--brand-blue);font-size:20px;letter-spacing:.5px}
.promo-text{left:768px;top:1636px;width:260px;font-size:12.5px;line-height:19px;color:var(--muted)}
.promo-btn{left:770px;top:1772px;width:168px;height:40px;font-size:14px}

/* info */
.info-panel{left:0;top:1956px;width:714px;height:422px;background:var(--grey-panel)}
.info-photo{left:714px;top:1956px;width:354px;height:422px;background:linear-gradient(180deg,#d9dadb 0%,#c9cccf 55%,#8f8a82 80%,#6e6a66 100%)}
.info-title{left:170px;top:2006px;color:var(--brand-blue);font-size:20px;letter-spacing:.5px}
.info-list{left:188px;top:2058px;list-style:none}
.info-list li{display:flex;align-items:center;gap:16px;font-size:14px;color:var(--ink);height:36px}
.call-block{left:176px;top:2256px;display:flex;align-items:center;gap:16px}
.call-block .label{font-size:11px;font-weight:700;color:var(--navy)}
.call-block .number{font-family:"Montserrat",Arial,sans-serif;font-weight:700;font-size:25px;color:var(--brand-blue);line-height:28px}

/* gallery */
.gallery-photo{top:2386px;width:288px;height:240px}
.g1{left:8px;background:linear-gradient(135deg,#4b4848,#9a8376 50%,#d8d1c8)}
.g2{left:308px;background:linear-gradient(135deg,#8a8a7a,#d1c1b1 50%,#7d8a5e)}
.g3{left:606px;background:linear-gradient(135deg,#cfd2c6,#a99bb8 50%,#e7d4d0)}
.g4{left:904px;background:linear-gradient(135deg,#d8d8d2,#b09a7c 50%,#7c5d74)}
.gallery-arrow{top:2490px}

/* footer */
.site-footer{left:0;top:2636px;width:1200px;height:354px;background:var(--footer-blue);color:var(--white)}
.footer-brand{left:130px;top:2700px;display:flex;flex-direction:column;align-items:center;width:264px}
.footer-brand .brand-square{background:var(--white);width:52px;height:52px;margin-bottom:16px}
.footer-brand .brand-name{color:var(--white);font-size:30px}
.footer-brand .brand-tag{color:var(--white);font-size:12px;margin-top:6px}
.footer-head{top:2684px;font-size:11px;font-weight:700;letter-spacing:.5px;color:var(--white)}
.footer-contact{left:472px;top:2716px;font-size:11px;line-height:17px;color:var(--white)}
.footer-contact .row{display:flex;gap:14px;margin-bottom:18px}
.footer-menu{left:722px;top:2714px;list-style:none;font-size:11px;line-height:17.6px}
.news-input{left:864px;top:2726px;width:206px;height:38px;background:var(--white);color:#888;font-size:11px;padding:0 14px;display:flex;align-items:center}
.news-btn{left:864px;top:2788px;width:74px;height:28px;background:#333;color:var(--white);font-size:11px;font-weight:700;display:flex;align-items:center;justify-content:center}
.footer-rule{left:130px;top:2880px;width:940px;height:1px;background:rgba(255,255,255,.25)}
.footer-follow{left:136px;top:2934px;display:flex;align-items:center;gap:12px;font-size:11px;font-weight:700}
.footer-follow .dots{gap:10px;margin-left:8px}
.footer-follow .dot{width:24px;height:24px}
.copyright{left:878px;top:2940px;width:192px;text-align:right;font-size:10px}
</style>
</head>
<body>

<header class="abs site-header">
  <div class="abs brand">
    <div class="brand-mark"><span class="brand-square"></span><span class="brand-name">Willowbrook Elders</span></div>
    <span class="brand-tag">Junior Seniors assisting Senior Seniors</span>
  </div>
  <div class="abs call-now">
    <svg width="30" height="30" viewBox="0 0 30 30"><circle cx="15" cy="15" r="13" fill="none" stroke="#1d3a75" stroke-width="1.5"/><path d="M10 8c1 0 2 3 2 4s-1 1.5-1 2c0 1 3 4.5 5 5 .5 0 1-1 2-1s4 1 4 2-1 3-3 3c-5 0-11-7-11-12 0-2 1-3 2-3z" fill="#1d3a75"/></svg>
    <div><div class="label">CALL US NOW</div><div class="number">555-014-2290</div></div>
  </div>
  <div class="abs follow">
    <div class="label">FOLLOW US</div>
    <div class="dots"><span class="dot" style="background:#2e5aa8"></span><span class="dot" style="background:#2aa3e0"></span><span class="dot" style="background:#1d3a75"></span></div>
  </div>
  <nav class="abs main-nav">
    <a class="active" href="#">HOME</a><a href="#">SERVICES</a><a href="#">ABOUT US</a><a href="#">NEWS</a><a href="#">EMPLOYMENT</a><a href="#">CONTACT US</a>
  </nav>
</header>

<section>
  <div class="abs hero" role="img" aria-label="Photo of two smiling senior women sharing a laugh on a porch"></div>
  <div class="abs hero-shade"></div>
  <div class="abs hero-arrow" style="left:0"><svg width="12" height="16"><path d="M9 2 3 8l6 6" stroke="#fff" stroke-width="2.5" fill="none"/></svg></div>
  <div class="abs hero-arrow" style="left:1166px"><svg width="12" height="16"><path d="M3 2l6 6-6 6" stroke="#fff" stroke-width="2.5" fill="none"/></svg></div>
  <h1 class="abs heading hero-title">Non medical, in home and away<br>care and companionship</h1>
  <a class="abs btn-red hero-btn">Download Brochure</a>
</section>

<section>
  <h2 class="abs heading section-title" style="top:686px">OUR SERVICES</h2>
  <div class="abs title-rule" style="top:730px"></div>
  <svg class="abs carousel-arrow" style="left:52px" width="16" height="30"><path d="M14 2 3 15l11 13" stroke="#999" stroke-width="2" fill="none"/></svg>
  <svg class="abs carousel-arrow" style="left:1136px" width="16" height="30"><path d="M2 2l11 13L2 28" stroke="#999" stroke-width="2" fill="none"/></svg>

  <div class="abs service" style="left:122px"><svg width="52" height="52" viewBox="0 0 52 52"><path d="M6 18h40l-4-10H10z" fill="#3277b5"/><rect x="10" y="20" width="32" height="22" fill="#3277b5"/><rect x="16" y="26" width="8" height="16" fill="#fff"/><rect x="28" y="26" width="10" height="8" fill="#fff"/></svg>Grocery Shopping</div>
  <div class="abs service" style="left:270px"><svg width="52" height="52" viewBox="0 0 52 52"><rect x="12" y="6" width="28" height="38" rx="3" fill="#3277b5"/><circle cx="26" cy="28" r="9" fill="#fff"/><circle cx="26" cy="28" r="5" fill="#3277b5"/><rect x="16" y="10" width="8" height="3" fill="#fff"/></svg>Laundry</div>
  <div class="abs service" style="left:398px"><svg width="52" height="52" viewBox="0 0 52 52"><ellipse cx="26" cy="36" rx="20" ry="6" fill="none" stroke="#3277b5" stroke-width="3"/><path d="M20 34c0-8 3-14 6-22 3 8 6 14 6 22z" fill="#3277b5"/></svg>Hobbies</div>
  <div class="abs service" style="left:528px"><svg width="52" height="52" viewBox="0 0 52 52"><circle cx="26" cy="14" r="9" fill="#3277b5"/><path d="M10 44c0-10 7-16 16-16s16 6 16 16z" fill="#3277b5"/><rect x="16" y="32" width="20" height="8" fill="#fff"/></svg>Reading</div>
  <div class="abs service" style="left:662px"><svg width="60" height="52" viewBox="0 0 60 52"><rect x="4" y="14" width="52" height="24" rx="4" fill="#3277b5"/><rect x="10" y="18" width="10" height="8" fill="#fff"/><rect x="24" y="18" width="10" height="8" fill="#fff"/><rect x="38" y="18" width="10" height="8" fill="#fff"/><circle cx="16" cy="40" r="5" fill="#3277b5" stroke="#fff" stroke-width="2"/><circle cx="44" cy="40" r="5" fill="#3277b5" stroke="#fff" stroke-width="2"/></svg>Transportation</div>
  <div class="abs service" style="left:817px"><svg width="52" height="52" viewBox="0 0 52 52"><circle cx="26" cy="22" r="10" fill="none" stroke="#3277b5" stroke-width="3"/><rect x="21" y="34" width="10" height="8" fill="#3277b5"/><path d="M26 2v5M8 10l4 4M44 10l-4 4M4 22h5M43 22h5" stroke="#3277b5" stroke-width="2.5"/></svg>Light housekeeping</div>
  <div class="abs service" style="left:963px"><svg width="60" height="52" viewBox="0 0 60 52"><path d="M6 10v32M54 28v14M6 34h48" stroke="#3277b5" stroke-width="3.5"/><rect x="6" y="24" width="48" height="10" fill="#3277b5"/><rect x="12" y="16" width="12" height="8" rx="2" fill="#3277b5"/></svg>Bed Making</div>
</section>

<section>
  <div class="abs band-left"></div>
  <div class="abs band-right"></div>
  <div class="abs band-photo" role="img" aria-label="Photo of a caregiver handing a mug to a seated senior woman in a living room"></div>
  <div class="abs band-text">
    <h2>Become a Junior Senior</h2>
    <div class="sub">Are you looking for a rewarding way to give back to the community?</div>
    <p>Many Junior Seniors join Willowbrook Elders just before they retire or once they are fully retired. They come to us with decades of life experiences and a host of professional skills in nursing, teaching, business, social services, home management and government, to name just a few categories.</p>
  </div>
  <a class="abs btn-white">READ MORE</a>
  <div class="abs benefits-label">Benefits</div>
  <div class="abs benefits-rule"></div>
  <div class="abs benefit" style="left:132px;top:1306px"><svg width="12" height="10"><path d="M1 1l4 4-4 4M6 1l4 4-4 4" stroke="#fff" stroke-width="1.5" fill="none"/></svg><span>Choose how many part time hours per week you would like to work (up to 29)</span></div>
  <div class="abs benefit" style="left:356px;top:1306px;width:170px"><svg width="12" height="10"><path d="M1 1l4 4-4 4M6 1l4 4-4 4" stroke="#fff" stroke-width="1.5" fill="none"/></svg><span>Give back to your community</span></div>
  <div class="abs benefit" style="left:552px;top:1306px;width:150px"><svg width="12" height="10"><path d="M1 1l4 4-4 4M6 1l4 4-4 4" stroke="#fff" stroke-width="1.5" fill="none"/></svg><span>Supplement your income</span></div>
  <div class="abs benefit" style="left:132px;top:1384px"><svg width="12" height="10"><path d="M1 1l4 4-4 4M6 1l4 4-4 4" stroke="#fff" stroke-width="1.5" fill="none"/></svg><span>Get paid for<br>"volunteer" work</span></div>
  <div class="abs benefit" style="left:356px;top:1384px;width:170px"><svg width="12" height="10"><path d="M1 1l4 4-4 4M6 1l4 4-4 4" stroke="#fff" stroke-width="1.5" fill="none"/></svg><span>Achieve fulfillment by helping others</span></div>
  <div class="abs benefit" style="left:552px;top:1384px;width:150px"><svg width="12" height="10"><path d="M1 1l4 4-4 4M6 1l4 4-4 4" stroke="#fff" stroke-width="1.5" fill="none"/></svg><span>Add meaning to your life</span></div>
</section>

<section>
  <div class="abs video-panel"></div>
  <div class="abs video-thumb" role="img" aria-label="Video still of a grandfather reading a picture book with two young children"></div>
  <svg class="abs play" width="80" height="80" viewBox="0 0 80 80"><circle cx="40" cy="40" r="40" fill="#ec1f27"/><path d="M32 24v32l26-16z" fill="#fff"/></svg>
  <h2 class="abs heading promo-title">PROMOTIONAL VIDEO</h2>
  <p class="abs promo-text">There are many variations of passages of Lorem Ipsum available, but the majority have suffered alteration in some form, by injected humour, or randomised words which don't look even slightly believable.</p>
  <a class="abs btn-red promo-btn">Watch Video</a>
</section>

<section>
  <div class="abs info-panel"></div>
  <div class="abs info-photo" role="img" aria-label="Photo of two senior women walking together outside a house"></div>
  <h2 class="abs heading info-title">WILLOWBROOK ELDERS</h2>
  <ul class="abs info-list">
    <li><svg width="12" height="10"><path d="M1 1l4 4-4 4M6 1l4 4-4 4" stroke="#3277b5" stroke-width="1.5" fill="none"/></svg>Junior Seniors assisting Senior Seniors</li>
    <li><svg width="12" height="10"><path d="M1 1l4 4-4 4M6 1l4 4-4 4" stroke="#3277b5" stroke-width="1.5" fill="none"/></svg>Why non-medical in-home care?</li>
    <li><svg width="12" height="10"><path d="M1 1l4 4-4 4M6 1l4 4-4 4" stroke="#3277b5" stroke-width="1.5" fill="none"/></svg>The financial effects of senior care</li>
    <li><svg width="12" height="10"><path d="M1 1l4 4-4 4M6 1l4 4-4 4" stroke="#3277b5" stroke-width="1.5" fill="none"/></svg>Do you need assistance?</li>
    <li><svg width="12" height="10"><path d="M1 1l4 4-4 4M6 1l4 4-4 4" stroke="#3277b5" stroke-width="1.5" fill="none"/></svg>Does a loved one need assistance?</li>
  </ul>
  <div class="abs call-block">
    <svg width="38" height="38" viewBox="0 0 38 38"><circle cx="19" cy="19" r="19" fill="#ec1f27"/><path d="M13 10c1 0 2.5 3.5 2.5 4.5S14 16 14 16.5c0 1.5 4 6 6 6.5.5 0 1-1.5 2-1.5s5 1.5 5 2.5-1 3.5-3.5 3.5C17 27.5 10 20 10 14c0-2.5 1.5-4 3-4z" fill="#fff"/></svg>
    <div><div class="label">CALL</div><div class="number">555-014-2290 Today!</div></div>
  </div>
</section>

<section>
  <div class="abs gallery-photo g1" role="img" aria-label="Photo of a senior couple looking at a laptop together"></div>
  <div class="abs gallery-photo g2" role="img" aria-label="Photo of two senior women smiling closely together"></div>
  <div class="abs gallery-photo g3" role="img" aria-label="Photo of two senior women talking at a table"></div>
  <div class="abs gallery-photo g4" role="img" aria-label="Photo of a caregiver bringing a basket of groceries to a senior woman"></div>
  <svg class="abs gallery-arrow" style="left:18px" width="14" height="20"><path d="M11 2 3 10l8 8" stroke="#fff" stroke-width="2.5" fill="none"/></svg>
  <svg class="abs gallery-arrow" style="left:1166px" width="14" height="20"><path d="M3 2l8 8-8 8" stroke="#fff" stroke-width="2.5" fill="none"/></svg>
</section>

<footer class="abs site-footer"></footer>
<div class="abs footer-brand">
  <span class="brand-square"></span>
  <span class="brand-name">Willowbrook Elders</span>
  <span class="brand-tag">Junior Seniors assisting Senior Seniors</span>
</div>
<div class="abs footer-head" style="left:476px">CONTACT US</div>
<div class="abs footer-contact">
  <div class="row"><svg width="10" height="14" viewBox="0 0 10 14"><path d="M5 0a5 5 0 0 0-5 5c0 4 5 9 5 9s5-5 5-9a5 5 0 0 0-5-5z" fill="#fff"/><circle cx="5" cy="5" r="2" fill="#2e62a9"/></svg><span>P.O. Box 48, Maple Hollow,<br>New York 10000</span></div>
  <div class="row"><svg width="10" height="12" viewBox="0 0 10 12"><path d="M2 0c1 0 2 2.5 2 3S3 4 3 4.5c0 1 2 3.5 3 3.5.5 0 .5-1 1.5-1S10 8.5 10 9s-.5 3-2 3C4 12 0 7 0 3c0-2 1-3 2-3z" fill="#fff"/></svg><span>555-014-7735</span></div>
  <div class="row"><svg width="12" height="10" viewBox="0 0 12 10"><rect width="12" height="10" fill="#fff"/><path d="M0 0l6 5 6-5" stroke="#2e62a9" fill="none"/></svg><span>hello@willowbrook-elders.com</span></div>
</div>
<div class="abs footer-head" style="left:722px">MENU</div>
<ul class="abs footer-menu">
  <li>Home</li><li>Services</li><li>About Us</li><li>News</li><li>Employment</li><li>Contact us</li>
</ul>
<div class="abs footer-head" style="left:864px">NEWSLETTER</div>
<div class="abs news-input">E-mail id</div>
<div class="abs news-btn">SIGNUP</div>
<div class="abs footer-rule"></div>
<div class="abs footer-follow" style="color:#fff">FOLLOW US
  <div class="dots"><span class="dot" style="background:#2a4f94"></span><span class="dot" style="background:#2aa3e0"></span><span class="dot" style="background:#1d3a75"></span></div>
</div>
<div class="abs copyright" style="color:#fff">Copyrights @ 2017 All Rights Reserved</div>

</body>
</html>
```